Valdarossi’s Artisan Pizzeria Menu Contest

I’m looking for a menu design for a new pizzeria - it’s farm to table type of restaurant - more upscale than a typical pizzeria - white washed wood interior with some industrial accents - I am looking for a creative menu layout using the attached sample menu items -
Valdarossi’s is an artisanal pizzeria with an atmosphere that will make you feel at home for any situation, first date, anniversary, business lunch, boys night out or girls night out with a menu inspired by the idea of a simple honest cooking paired with fresh – quality ingredients. Full service dining experience that is still casual but dedicated to extraordinary hospitality.
While developing the menu we have created a network of amazing farms and purveyors to supply our restaurant with fresh milled 100% California flour for our hand crafted dough, as well as sustainably farmed organic produce, meats and cheeses.
The menu includes classics like the Margherita pizza to daily seasonal specials, fresh salads to rustic small plates including moms meatball recipe to a fresh local burrata with handmade bread. Each dish reflects our passion for sourcing the freshest quality local ingredients.
To compliment the menu, Valdarossi’s serves an extensive wine list with selections focusing on Italian varietals. The cocktail program has been carefully crafted to offer something to entice ever palate and the beer list has unique selections of the world’s finest brewers.
Target Market(s)
25-45 year old men and women
Industry/Entity Type
American Restaurant
Requirements
Must have
- professional tone
Nice to have
- a balance of elegance and industrial (rustic)
Should not have
- photos or playful graphics etc..

```html
<!DOCTYPE html>
<html lang="en">
<head>
<meta charset="utf-8">
<title>Valdarossi’s Artisan Pizzeria Menu</title>
<link href="https://fonts.googleapis.com/css2?family=Josefin+Sans:wght@400;600;700&family=Cormorant+Garamond:ital,wght@1,400;1,500&display=swap" rel="stylesheet">
<style>
:root{
  --stage:#bcc6c9;
  --plum:#230c19;
  --paper:#ffffff;
  --wood-a:#e9e1d6;
  --wood-b:#d8cdbd;
  --card:#f7f5f2;
  --price:#e2413a;
  --rose:#e8a898;
  --ink:#2a2a2a;
  --muted:#6f6a66;
}
*{box-sizing:border-box;margin:0;padding:0}
html,body{width:1200px;height:1200px;overflow:hidden}
body{background:var(--stage);position:relative;font-family:"Josefin Sans",sans-serif;color:var(--ink)}

/* ---------- cover spread ---------- */
.cover{position:absolute;left:40px;top:178px;width:550px;height:710px;display:flex;box-shadow:0 18px 30px rgba(0,0,0,.25)}
.drinks{width:275px;height:100%;background:var(--plum);position:relative}
.drinks-frame{position:absolute;left:24px;top:24px;right:24px;bottom:24px;border:1.5px solid #fff;border-radius:8px}
.drink-section{position:absolute;left:0;right:0}
.drink-pill{position:absolute;left:78px;width:118px;height:15px;background:#fff;color:var(--plum);font-weight:600;font-size:11px;text-align:center;line-height:16px;letter-spacing:.5px;
  clip-path:polygon(7px 0,calc(100% - 7px) 0,100% 50%,calc(100% - 7px) 100%,7px 100%,0 50%)}
.drink-icon{position:absolute;left:123px}
.drink-list{position:absolute;left:55px;width:180px;display:grid;grid-template-columns:1fr 1fr;column-gap:0;row-gap:0}
.drink-list span{font-family:"Cormorant Garamond",serif;font-style:italic;color:#fff;font-size:10px;line-height:17px}
.drink-list span b{font-family:"Josefin Sans",sans-serif;font-style:normal;font-weight:600;font-size:8px;margin-left:4px}

.front{flex:1;position:relative;background:linear-gradient(90deg,var(--wood-b),var(--wood-a) 20%,var(--wood-b) 45%,var(--wood-a) 70%,var(--wood-b))}
.front-frame{position:absolute;left:21px;top:24px;right:24px;bottom:24px;border:1.5px solid #7d756e}
.front-frame::after{content:"";position:absolute;inset:3px;border:1px solid #9b938b}
.corner{position:absolute;width:12px;height:12px;border-radius:50%;background:#3a2c2a}
.front-card{position:absolute;left:42px;top:40px;width:190px;height:628px;background:var(--card);
  clip-path:polygon(14px 0,calc(100% - 14px) 0,100% 14px,100% calc(100% - 14px),calc(100% - 14px) 100%,14px 100%,0 calc(100% - 14px),0 14px)}
.brand{position:absolute;left:0;right:0;top:150px;text-align:center;font-family:"Josefin Sans",sans-serif;font-weight:700;font-size:26px;color:var(--plum);letter-spacing:.5px}
.flourish{position:absolute;left:55px;width:110px;height:40px;background:linear-gradient(90deg,transparent,#cfc9c4 30%,#cfc9c4 70%,transparent);opacity:.7;border-radius:20px}
.menu-word{position:absolute;left:0;right:0;top:330px;text-align:center;font-weight:400;font-size:40px;color:var(--plum);letter-spacing:2px}

/* ---------- inside spread ---------- */
.inside{position:absolute;left:612px;top:177px;width:552px;height:713px;background:var(--plum);box-shadow:0 18px 30px rgba(0,0,0,.25)}
.inside-paper{position:absolute;left:9px;top:13px;width:532px;height:688px;background:var(--paper)}
.col{position:absolute;top:12px;width:227px;height:664px;border:1.5px solid var(--rose);
  clip-path:polygon(8px 0,calc(100% - 8px) 0,100% 8px,100% calc(100% - 8px),calc(100% - 8px) 100%,8px 100%,0 calc(100% - 8px),0 8px);
  text-align:center;padding:0 6px}
.col-left{left:16px}
.col-right{left:292px}
.col::before{content:"";position:absolute;inset:0;border:1.5px solid var(--rose);pointer-events:none}
.pill{display:block;margin:0 auto;width:120px;height:15px;background:var(--plum);color:#fff;font-weight:600;font-size:11px;line-height:16px;letter-spacing:.6px;
  clip-path:polygon(7px 0,calc(100% - 7px) 0,100% 50%,calc(100% - 7px) 100%,7px 100%,0 50%)}
.item{margin-top:7px}
.item-name{font-variant:small-caps;font-weight:600;font-size:10.5px;letter-spacing:.4px;color:#333;line-height:12px}
.price{color:var(--price);font-variant:normal;font-weight:400;font-size:9.5px;margin-left:3px}
.item-desc{font-family:"Cormorant Garamond",serif;font-style:italic;font-size:9.6px;line-height:12.8px;color:#3d3a38}
.soup{margin:8px 2px 0;border:1.5px dotted #aaa;padding:4px 0 3px;font-variant:small-caps;font-size:11px;font-weight:600}
.soup .note{font-weight:400}
.crusts{margin-top:10px;border:1.5px dotted #aaa;padding:2px 0 3px}
.crusts-title{font-weight:700;font-size:12px;letter-spacing:.5px}
.crusts-row{display:flex;margin-top:4px}
.crusts-row>div{flex:1}
.crusts-row>div+div{border-left:1.5px dotted #aaa}
.dips-title{margin-top:8px;font-weight:700;font-size:11.5px;display:flex;align-items:center;gap:6px}
.dips-title::before,.dips-title::after{content:"";flex:1;border-top:1.5px dotted #aaa}
.dips{display:flex;justify-content:center;align-items:center;gap:6px;margin-top:6px}
.dot{width:4px;height:4px;border-radius:50%;background:var(--price)}
</style>
</head>
<body>

<section class="cover">
  <div class="drinks">
    <div class="drinks-frame"></div>

    <div class="drink-section" style="top:0">
      <div class="drink-pill" style="top:35px">BEER</div>
      <div class="drink-icon" role="img" aria-label="Wheat stalk emblem" style="top:54px;width:28px;height:30px;background:radial-gradient(circle,#fff 30%,transparent 70%);opacity:.8"></div>
      <div class="drink-list" style="top:84px">
        <span>Lorem Ipsum<b>$</b></span><span>Lorem Ipsum<b>$</b></span>
        <span>Lorem Ipsum<b>$</b></span><span>Lorem Ipsum<b>$</b></span>
        <span>Lorem Ipsum<b>$</b></span><span>Lorem Ipsum<b>$</b></span>
        <span>Lorem Ipsum<b>$</b></span><span>Lorem Ipsum<b>$</b></span>
        <span>Lorem Ipsum<b>$</b></span><span>Lorem Ipsum<b>$</b></span>
        <span>Lorem Ipsum<b>$</b></span><span>Lorem Ipsum<b>$</b></span>
        <span>Lorem Ipsum<b>$</b></span><span>Lorem Ipsum<b>$</b></span>
        <span>Lorem Ipsum<b>$</b></span><span>Lorem Ipsum<b>$</b></span>
        <span>Lorem Ipsum<b>$</b></span><span>Lorem Ipsum<b>$</b></span>
      </div>
    </div>

    <div class="drink-section" style="top:0">
      <div class="drink-pill" style="top:247px">COCKTAILS</div>
      <svg class="drink-icon" style="top:266px;left:127px" width="22" height="38" viewBox="0 0 22 38">
        <path d="M1 1 H21 L11 15 Z" fill="#fff"/>
        <line x1="11" y1="15" x2="11" y2="34" stroke="#fff" stroke-width="1.5"/>
        <line x1="5" y1="35" x2="17" y2="35" stroke="#fff" stroke-width="2"/>
      </svg>
      <div class="drink-list" style="top:296px">
        <span>Lorem Ipsum<b>$</b></span><span>Lorem Ipsum<b>$</b></span>
        <span>Lorem Ipsum<b>$</b></span><span>Lorem Ipsum<b>$</b></span>
        <span>Lorem Ipsum<b>$</b></span><span>Lorem Ipsum<b>$</b></span>
        <span>Lorem Ipsum<b>$</b></span><span>Lorem Ipsum<b>$</b></span>
        <span>Lorem Ipsum<b>$</b></span><span>Lorem Ipsum<b>$</b></span>
        <span>Lorem Ipsum<b>$</b></span><span>Lorem Ipsum<b>$</b></span>
        <span>Lorem Ipsum<b>$</b></span><span>Lorem Ipsum<b>$</b></span>
        <span>Lorem Ipsum<b>$</b></span><span>Lorem Ipsum<b>$</b></span>
        <span>Lorem Ipsum<b>$</b></span><span>Lorem Ipsum<b>$</b></span>
      </div>
    </div>

    <div class="drink-section" style="top:0">
      <div class="drink-pill" style="top:461px">WINES</div>
      <svg class="drink-icon" style="top:481px;left:125px" width="26" height="34" viewBox="0 0 26 34">
        <rect x="1" y="1" width="24" height="4" rx="2" fill="#fff"/>
        <rect x="11" y="5" width="4" height="6" fill="#fff"/>
        <path d="M13 11 q4 2 0 4 q-4 2 0 4 q4 2 0 4 q-4 2 0 4 q4 2 0 4" stroke="#fff" stroke-width="1.3" fill="none"/>
      </svg>
      <div class="drink-list" style="top:511px">
        <span>Lorem Ipsum<b>$</b></span><span>Lorem Ipsum<b>$</b></span>
        <span>Lorem Ipsum<b>$</b></span><span>Lorem Ipsum<b>$</b></span>
        <span>Lorem Ipsum<b>$</b></span><span>Lorem Ipsum<b>$</b></span>
        <span>Lorem Ipsum<b>$</b></span><span>Lorem Ipsum<b>$</b></span>
        <span>Lorem Ipsum<b>$</b></span><span>Lorem Ipsum<b>$</b></span>
        <span>Lorem Ipsum<b>$</b></span><span>Lorem Ipsum<b>$</b></span>
        <span>Lorem Ipsum<b>$</b></span><span>Lorem Ipsum<b>$</b></span>
        <span>Lorem Ipsum<b>$</b></span><span>Lorem Ipsum<b>$</b></span>
        <span>Lorem Ipsum<b>$</b></span><span>Lorem Ipsum<b>$</b></span>
      </div>
    </div>
  </div>

  <div class="front" role="img" aria-label="Whitewashed wood plank background">
    <div class="front-frame"></div>
    <div class="corner" role="img" aria-label="Corner ornament" style="left:28px;top:32px"></div>
    <div class="corner" role="img" aria-label="Corner ornament" style="right:30px;top:32px"></div>
    <div class="corner" role="img" aria-label="Corner ornament" style="left:28px;bottom:32px"></div>
    <div class="corner" role="img" aria-label="Corner ornament" style="right:30px;bottom:32px"></div>
    <div class="front-card">
      <div class="brand">Valdarossi’s</div>
      <div class="flourish" role="img" aria-label="Scroll flourish above title" style="top:282px"></div>
      <div class="menu-word">MENU</div>
      <div class="flourish" role="img" aria-label="Scroll flourish below title" style="top:390px"></div>
    </div>
  </div>
</section>

<section class="inside">
  <div class="inside-paper">

    <div class="col col-left">
      <span class="pill" style="margin-top:10px">APPETIZERS</span>
      <div class="item" style="margin-top:4px"><div class="item-name">Brussels<span class="price">$10.00</span></div>
        <div class="item-desc">Pan Seared Brussel Sprouts with a Drizzle of<br>Balsamic Reduction and Parm and Bread Crumbs</div></div>
      <div class="item"><div class="item-name">Meatballs<span class="price">$13.00</span></div>
        <div class="item-desc">Moms Meatballs handmade<br>secret recipe for over 75 years</div></div>
      <div class="item"><div class="item-name">Mussels<span class="price">$15.00</span></div>
        <div class="item-desc">New Zealand Mussels in a Tomato Broth</div></div>
      <div class="item"><div class="item-name">Romanesco<span class="price">$11.00</span></div>
        <div class="item-desc">Flash Fried Romanesco served atop a Spicy Aioli</div></div>
      <div class="item"><div class="item-name">Chicken Wings<span class="price">$10.00</span></div>
        <div class="item-desc">Italian Fried Chicken Wings With a Kick</div></div>
      <div class="item"><div class="item-name">Burrata<span class="price">$13.00</span></div>
        <div class="item-desc">Local Burrata served with Apples<br>Grapes and Fresh Made Bread</div></div>

      <span class="pill" style="margin-top:9px">SALADS</span>
      <div class="item" style="margin-top:4px"><div class="item-name">Chopped Salad<span class="price">$13.00</span></div>
        <div class="item-desc">Lettuce mix with Tomato, Onions, Peppers,<br>Pepperoni, Chick Peas, Fresh Mozz, Italian Herb Ving</div></div>
      <div class="item"><div class="item-name">Caesar Salad<span class="price">$11.00</span></div>
        <div class="item-desc">Traditional Caesar Salad Rich and<br>Creamy Extra Shaved Parmesan</div></div>
      <div class="item"><div class="item-name">Farm Salad<span class="price">$15.00</span></div>
        <div class="item-desc">Seasonal Farmers Market Salad</div></div>
      <div class="item"><div class="item-name">Grilled Little Gem<span class="price">$11.00</span></div>
        <div class="item-desc">Grilled Little Gems with Bacon, Tomato,<br>Red Onions and Blue Cheese Dressing</div></div>
      <div class="item"><div class="item-name">Spinach and Arugula Salad<span class="price">$12.00</span></div>
        <div class="item-desc">Spinach and Argula, Red Peppers tossed in a Lem-<br>on Ving and Housemade Croutons</div></div>

      <div class="soup">Daily Soup <span class="note">— Tomato Bisque</span><span class="price">$8.00</span></div>

      <span class="pill" style="margin-top:9px">SANDWICHES</span>
      <div class="item" style="margin-top:4px"><div class="item-name">Italian Sub<span class="price">$13.00</span></div>
        <div class="item-desc">Prociutto, Salumi, Turkey, Provolone, Lettuce,<br>Tomato and Herb Aioli with Spicy Gardenia</div></div>
      <div class="item"><div class="item-name">Turkey Sandwich<span class="price">$12.00</span></div>
        <div class="item-desc">Housemade Bread — Turkey, Cheddar Cheese, But-<br>ter Lettuce, Tomato and Mustard Aioli</div></div>
      <div class="item"><div class="item-name">Meatball sub<span class="price">$13.00</span></div>
        <div class="item-desc">Moms Meatballs Melted Provolone on a Housemade Roll</div></div>
    </div>

    <div class="col col-right">
      <div class="item" style="margin-top:10px"><div class="item-name">Harvest Burger<span class="price">$14.00</span></div>
        <div class="item-desc">Housemade Bun — Arugula , Tomato,<br>Onion and a Sundried Tomato Spread</div></div>
      <div class="item"><div class="item-name">Chicken Sanwich<span class="price">$13.00</span></div>
        <div class="item-desc">Fried Chicken or Chicken Breast, Provolone,<br>Argula, Tomato, served with a Spicy Aioli</div></div>

      <span class="pill" style="margin-top:9px">PIZZAS</span>
      <div class="item" style="margin-top:4px"><div class="item-name">Margherita<span class="price">$14.00</span></div>
        <div class="item-desc">Classic Margherita Pizza — Fresh Mozz<br>Tomato Sauce and Basil</div></div>
      <div class="item"><div class="item-name">Organic Sausage<span class="price">$16.00</span></div>
        <div class="item-desc">Organic Sausage Housemade Red Sauce<br>Mozz Hint of Fennel</div></div>
      <div class="item"><div class="item-name">Pepperoni<span class="price">$16.00</span></div>
        <div class="item-desc">Marlow Pepperoni — Housemade Red Sauce<br>Chile flakes and Mozz</div></div>
      <div class="item"><div class="item-name">Salumi and Burrata<span class="price">$17.00</span></div>
        <div class="item-desc">Salumi dried Red Sauce finished with Whipped Burrata</div></div>
      <div class="item"><div class="item-name">Daily Special<span class="price">$17.00</span></div></div>
      <div class="item"><div class="item-name">Mushroom<span class="price">$15.00</span></div>
        <div class="item-desc">Shaved Mushrooms with a Parmesan<br>cream and melted onions</div></div>
      <div class="item"><div class="item-name">Prosciutto and Egg<span class="price">$16.00</span></div>
        <div class="item-desc">Parma Prosciutto Parmesan cream with Emmental<br>and Gruyere finished with an Organic Egg</div></div>
      <div class="item"><div class="item-name">Quarttro Formaggi<span class="price">$15.00</span></div>
        <div class="item-desc">Four Cheese Combination — Mozz — Fontina — Parm<br>Cream and Gruyere Chile Flakes and Oregano</div></div>
      <div class="item"><div class="item-name">Farmers Pizza<span class="price">$17.00</span></div>
        <div class="item-desc">Seasonal Vegatables Cream Sauce and a Variety of Cheese</div></div>
      <div class="item" style="margin-top:5px"><div class="item-name">Keto Friendly<span class="price">$17.00</span></div>
        <div class="item-desc">Cauliflower Crust, Spinach and Kale, Parm Cream Sauce</div></div>

      <div class="crusts">
        <div class="crusts-title">CRUSTS</div>
        <div class="item" style="margin-top:3px"><div class="item-name">Traditional</div>
          <div class="item-desc">Orginal crust you can't miss</div></div>
        <div class="crusts-row">
          <div><div class="item-name">Gluten Free<span class="price">$3.00</span></div>
            <div class="item-desc">Best gluten friendly crust<br>on the west coast</div></div>
          <div><div class="item-name">Cauliflower<span class="price">$3.00</span></div>
            <div class="item-desc">Vegans have needs</div></div>
        </div>
      </div>

      <div class="dips-title"><span>DIPS <span class="price">$1.00</span></span></div>
      <div class="dips item-desc">
        <span>Ranch</span><span class="dot"></span><span>Tomato Sauce</span><span class="dot"></span><span>Spicy Dip</span><span class="dot"></span><span>Blue Cheese</span>
      </div>
    </div>

  </div>
</section>

</body>
</html>
```